Surgical Procedure Room Letterhead

PLEASE DO NOT MAKE YOUR LETTERHEAD SIMILAR TO THE ONE I AM INCLUDING IN MY UPLOADS

Hello! I need my logo used to make a very clean, professional, simple letterhead that has all the pertinent information in it:
Location: 4182 NW 38th Lane, Suite 500
Harbor Glen, OR 33967
Phone: 954-218-4650
Fax: 800-642-9082

Can you please put this all on a word document that is easily editable? I will include my practice letterhead as an example ONLY of how easy it should be to write below the letterhead. Please don't make this letterhead the same as the one I am including in this example. They are two separate businesses.

Target Market(s)

Insurance companies

Industry/Entity Type

medical

Requirements
Must have
• classiness, elegance, simplicity
Should not have
• Please don't make your letterhead the same as the one that I included in my uploads

```html
<!DOCTYPE html>
<html lang="en">
<head>
<meta charset="utf-8">
<title>Clinic Suites Letterhead</title>
<link href="https://fonts.googleapis.com/css2?family=Montserrat:wght@400;500;700&display=swap" rel="stylesheet">
<style>
  :root {
    --gold: #d6b03c;
    --ink: #1b1b1b;
    --body: #2a2a2a;
    --black-band: #121212;
    --paper: #ffffff;
    --sig-tone: #e9e9e9;
  }
  * { margin: 0; padding: 0; box-sizing: border-box; }
  html, body { width: 1023px; height: 1200px; overflow: hidden; background: var(--paper); }
  body { font-family: "Montserrat", sans-serif; color: var(--ink); }
  .letterhead { position: relative; width: 1023px; height: 1200px; background: var(--paper); }

  .brand { position: absolute; left: 80px; top: 92px; display: flex; align-items: center; gap: 18px; }
  .brand-dot { width: 58px; height: 58px; border-radius: 50%; background: var(--gold); }
  .brand-name { font-size: 50px; font-weight: 700; color: var(--gold); letter-spacing: 1px; }

  .sender { position: absolute; left: 106px; top: 352px; }
  .sender-name { font-size: 44px; font-weight: 700; color: var(--gold); line-height: 1; }
  .sender-role { font-size: 20px; font-weight: 400; margin-top: 14px; margin-left: 3px; }

  .contact-list { position: absolute; left: 109px; top: 456px; list-style: none; }
  .contact-item { display: flex; align-items: center; height: 32.5px; font-size: 20px; font-weight: 400; }
  .contact-icon { width: 22px; height: 22px; margin-right: 15px; fill: var(--gold); }

  .salutation { position: absolute; left: 111px; top: 580px; font-size: 21px; font-weight: 400; }
  .letter-date { position: absolute; right: 117px; top: 582px; font-size: 21px; font-weight: 400; }

  .letter-body { position: absolute; left: 113px; top: 632px; width: 800px; }
  .letter-body p { font-size: 15.5px; line-height: 19px; color: var(--body); margin-bottom: 18.5px; }

  .closing { position: absolute; left: 113px; top: 964px; font-size: 20px; font-weight: 400; }
  .signature { position: absolute; left: 112px; top: 1010px; width: 180px; height: 56px; background: var(--sig-tone); border-radius: 4px; }

  .address { position: absolute; left: 600px; top: 1003px; font-size: 18.5px; font-weight: 400; font-style: normal; line-height: 19px; }

  .footer-band { position: absolute; left: 0; bottom: 0; width: 100%; height: 50px; display: flex; }
  .footer-band .band-dark { width: 592px; background: var(--black-band); }
  .footer-band .band-gold { flex: 1; background: var(--gold); }
</style>
</head>
<body>
<div class="letterhead">
  <header class="brand">
    <div class="brand-dot"></div>
    <div class="brand-name">Clinic Suites</div>
  </header>

  <section class="sender">
    <div class="sender-name">Daniel Reyes</div>
    <div class="sender-role">Owner</div>
  </section>

  <ul class="contact-list">
    <li class="contact-item">
      <svg class="contact-icon" viewBox="0 0 24 24" aria-hidden="true"><path d="M3 8c0-2 4-4 9-4s9 2 9 4v2h-5V8.5c-1-.6-2.4-.9-4-.9s-3 .3-4 .9V10H3z"/><path d="M6 11h12l2 9H4z"/><circle cx="12" cy="15.5" r="2.4" fill="#fff"/></svg>
      954-218-4650
    </li>
    <li class="contact-item">
      <svg class="contact-icon" viewBox="0 0 24 24" aria-hidden="true"><rect x="6" y="3" width="12" height="5"/><path d="M3 9h18v8h-3v-3H6v3H3z"/><rect x="7" y="15" width="10" height="6"/></svg>
      800-642-9082
    </li>
    <li class="contact-item">
      <svg class="contact-icon" viewBox="0 0 24 24" aria-hidden="true"><path d="M2 5h20v2l-10 6L2 7z"/><path d="M2 9l10 6 10-6v10H2z"/></svg>
      info@clinicsuites.com
    </li>
  </ul>

  <div class="salutation">Dear Sir,</div>
  <div class="letter-date">Sep-28-2024</div>

  <main class="letter-body">
    <p>Lorem ipsum dolor sit amet, consectetur adipiscing elit, sed do eiusmod tempor incididunt ut labore et dolore magna aliqua. Quis ipsum suspendisse ultrices gravida. Risus commodo viverra maecenas accumsan lacus vel facilisis. Lorem ipsum dolor sit amet, consectetur adipiscing elit, sed do eiusmod tempor incididunt ut labore et dolore magna aliqua. Quis ipsum suspendisse ultrices gravida.</p>
    <p>Lorem ipsum dolor sit amet, consectetur adipiscing elit, sed do eiusmod tempor incididunt ut labore et dolore magna aliqua.Quis ipsum suspendisse ultrices gravida. Risus commodo viverra maecenas accumsan lacus vel facilisis. Lorem ipsum dolor sit amet, consectetur adipiscing elit, sed do eiusmod tempor incididunt ut labore et dolore magna aliqua. Quis ipsum suspendisse ultrices gravida. Risus commodo viverra maecenas accumsan lacus vel facilisis.</p>
    <p>Lorem ipsum dolor sit amet, consectetur adipiscing elit, sed do eiusmod tempor incididunt ut labore et dolore magna aliqua. Quis ipsum suspendisse ultrices gravida. Risus commodo viverra maecenas accumsan lacus vel facilisis. Lorem ipsum dolor sit amet, consectetur adipiscing elit, sed do eiusmod tempor incididunt ut labore et dolore magna aliqua. Quis ipsum suspendisse ultrices gravida. Risus commodo viverra maecenas accumsan lacus vel facilisis.</p>
  </main>

  <div class="closing">Rgards</div>
  <div class="signature" role="img" aria-label="Handwritten signature of the sender"></div>

  <address class="address">
    4182 NW 38th Lane, Suite 500<br>
    Harbor Glen, OR 33967
  </address>

  <footer class="footer-band">
    <div class="band-dark"></div>
    <div class="band-gold"></div>
  </footer>
</div>
</body>
</html>
```